Halden & Pruitt Periodontics and Implant Solutions Business Card

We are a specialty dental practice- implants and periodontal surgery. We have just re-designed our logo and are building a new office and would like to re-design our business card. We are looking for something professional with a creative and artsy twist- something to stand out among the rest! Happy Designing!

I have uploaded all versions of our new logo and our current business card. We have 3 locations and 2 doctors.

Target Market(s)

55+

Industry/Entity Type

Dental

Contact Information for Business Card

Needs Names, logo, locations- professional and artsy!

Colors
0555a3
0592cd
34a7d7
3277b5
85cae6
85acd3
cee9f5
ecf7fb

Requirements
Must have
• our names:
• Thomas E. Halden D.M.D.
• Celia M. Pruitt D.M.D.
• Diplomate of the National Council of Gum Surgery
• Address locations:
• 462 W. Larkspur Avenue Suite 210B Plantation, FL 33871
• Tel: 954-318-2264 Fax: 954-318-2291
• 5127 Harlow Lane #C-4 Boca Raton, FL 33609
• Tel: 561-627-1958 Fax: 561-703-2816
• 274 Northwest 9th Street #412 Miami FL 33987
• Tel: 786-429-6153 Fax: 786-429-6170
Nice to have
• unique look
Should not have
• doesn't need QR like our current card has.

```html
<!DOCTYPE html>
<html lang="en">
<head>
<meta charset="utf-8">
<title>Halden &amp; Pruitt Business Card</title>
<link href="https://fonts.googleapis.com/css2?family=Questrial&family=Roboto:wght@400;500&display=swap" rel="stylesheet">
<style>
  :root {
    --navy: #232a6e;
    --grey: #6f7073;
    --band-grey: #8a8b8e;
    --paper: #ffffff;
    --backdrop: #e9e9ea;
    --ink: #5a5b5e;
  }
  * { margin: 0; padding: 0; box-sizing: border-box; }
  html, body { width: 1200px; height: 726px; overflow: hidden; }
  body {
    background: var(--backdrop);
    display: flex;
    align-items: center;
    justify-content: center;
    gap: 40px;
  }
  .card {
    position: relative;
    width: 550px;
    height: 314px;
    background: var(--paper);
    box-shadow: 0 4px 14px rgba(0,0,0,0.12);
    overflow: hidden;
    font-family: "Questrial", sans-serif;
  }
  .card-bands { position: absolute; inset: 0; }

  /* Front */
  .front-ring {
    position: absolute;
    left: 34px; top: 60px;
    width: 190px; height: 190px;
  }
  .front-info {
    position: absolute;
    left: 262px; top: 34px;
    color: var(--navy);
  }
  .brand-name {
    font-size: 31px;
    line-height: 1;
    letter-spacing: 0.5px;
    color: var(--navy);
  }
  .brand-tagline {
    font-size: 12.5px;
    color: var(--navy);
    margin-top: 2px;
  }
  .doctor {
    font-size: 19px;
    line-height: 1.05;
    color: var(--navy);
  }
  .doctors { margin-top: 12px; }
  .diplomate {
    font-family: "Roboto", sans-serif;
    font-size: 9px;
    color: var(--grey);
    margin-top: 6px;
  }
  .contact-list { margin-top: 14px; list-style: none; }
  .contact-list li {
    display: flex;
    align-items: center;
    gap: 9px;
    font-family: "Roboto", sans-serif;
    font-size: 13px;
    color: var(--ink);
    line-height: 1.45;
  }
  .contact-list svg { width: 12px; height: 12px; fill: var(--ink); }
  .website {
    position: absolute;
    right: 34px; bottom: 15px;
    font-family: "Roboto", sans-serif;
    font-size: 14px;
    letter-spacing: 0.4px;
    color: var(--paper);
  }

  /* Back */
  .back-lockup {
    position: absolute;
    left: 130px; top: 28px;
    display: flex;
    align-items: center;
    gap: 8px;
  }
  .back-lockup svg { width: 80px; height: 80px; }
  .back-lockup .brand-name { font-size: 27px; }
  .back-lockup .brand-tagline { font-size: 11px; }
  .locations {
    position: absolute;
    left: 150px; top: 128px;
    font-family: "Roboto", sans-serif;
    font-size: 12px;
    color: var(--ink);
    line-height: 1.35;
  }
  .location + .location { margin-top: 12px; }
  .location-phones { padding-left: 22px; }
  .label { color: var(--navy); }
</style>
</head>
<body>

  <section class="card card-front">
    <svg class="card-bands" viewBox="0 0 550 314" aria-hidden="true">
      <polygon points="0,278 550,262 550,314 0,314" fill="var(--band-grey)"/>
      <polygon points="180,270 550,168 550,314 160,314" fill="var(--navy)"/>
    </svg>
    <svg class="front-ring" viewBox="0 0 190 190" aria-hidden="true">
      <circle cx="95" cy="95" r="86" fill="none" stroke="var(--navy)" stroke-width="9"/>
    </svg>
    <div class="front-info">
      <div class="brand-name">HALDEN &amp; PRUITT</div>
      <div class="brand-tagline">Periodontics and Implant Solutions</div>
      <div class="doctors">
        <div class="doctor">Thomas E. Halden, D.M.D.</div>
        <div class="doctor">Celia M. Pruitt, D.M.D.</div>
      </div>
      <div class="diplomate">Diplomate of the National Council of Gum Surgery</div>
      <ul class="contact-list">
        <li>
          <svg viewBox="0 0 24 24"><path d="M6.6 10.8a15.1 15.1 0 0 0 6.6 6.6l2.2-2.2a1 1 0 0 1 1-.25 11.4 11.4 0 0 0 3.6.57 1 1 0 0 1 1 1V20a1 1 0 0 1-1 1A17 17 0 0 1 3 4a1 1 0 0 1 1-1h3.5a1 1 0 0 1 1 1c0 1.25.2 2.45.57 3.57a1 1 0 0 1-.25 1z"/></svg>
          954-318-2264
        </li>
        <li>
          <svg viewBox="0 0 24 24"><path d="M2 5h20v14H2z M4 7v.5l8 5 8-5V7l-8 5z" fill-rule="evenodd"/></svg>
          contactus@haldenperio.com
        </li>
      </ul>
    </div>
    <div class="website">www.haldenperio.com</div>
  </section>

  <section class="card card-back">
    <svg class="card-bands" viewBox="0 0 550 314" aria-hidden="true">
      <polygon points="0,300 550,270 550,314 0,314" fill="var(--navy)"/>
    </svg>
    <div class="back-lockup">
      <svg viewBox="0 0 80 80" aria-hidden="true">
        <circle cx="40" cy="40" r="35" fill="none" stroke="var(--navy)" stroke-width="5"/>
      </svg>
      <div>
        <div class="brand-name">HALDEN &amp; PRUITT</div>
        <div class="brand-tagline">Periodontics and Implant Solutions</div>
      </div>
    </div>
    <div class="locations">
      <div class="location">
        <div>462 W. Larkspur Avenue Suite 210B Plantation, FL 33871</div>
        <div class="location-phones"><span class="label">Tel:</span> 954-318-2264 <span class="label">| Fax:</span> 954-318-2291</div>
      </div>
      <div class="location">
        <div>274 Northwest 9th Street #412 Miami, FL 33987</div>
        <div class="location-phones"><span class="label">Tel:</span> 786-429-6153 <span class="label">| Fax:</span> 786-429-6170</div>
      </div>
      <div class="location">
        <div>5127 Harlow Lane #C-4 Boca Raton, FL 33609</div>
        <div class="location-phones"><span class="label">Tel:</span> 561-627-1958 <span class="label">| Fax:</span> 561-703-2816</div>
      </div>
    </div>
  </section>

</body>
</html>
```